QV Wager needs banner to promote sign-ups

We need to put a banner on the homepage of our betting app / site to promote users who visit the site to sign-up for the platform. We are the largest blockchain based sports betting exchange. Our main markets are (in order) PHL, GRC, DTW, & KVJ. Users can bet in ZMTK, ORB, or QV (our coin). It would be cool to feature those three coins if possible.
Our three main points we want to get to the user:
"Best Odds"
"Be the Bookmaker"
"Own the House"
We have provided images of our site and of our logos to incorporate in the site. One of the images shows the homepage of the site, this banner being designed will replace the small banners currently there if a user is not signed in. Additionally, we have included our sign-up page which shows the different ways users can sign in to the site (we want to show these options on the banner if possible).
Brand Book Filevault
https://www.filevaultshare.example/sh/kqm4rtw8pzlx2/BBB7hNpQwErTyUiOpAsDfGh3k?dl=0
Industry/Entity Type
Sports betting & Blockchain
Look and feel

```html
<!DOCTYPE html>
<html lang="en">
<head>
<meta charset="UTF-8">
<title>QV Wager — Sign-up Banner</title>
<link rel="stylesheet" href="https://fonts.googleapis.com/css2?family=Poppins:wght@400;600;700&display=swap">
<style>
  :root {
    --bg-deep: #060912;
    --bg-navy: #0d1530;
    --bg-glow: #17306a;
    --text-white: #ffffff;
    --accent-teal: #2fd8b8;
    --btn-start: #23d3c4;
    --btn-end: #1f6fe0;
    --coin-ring: #d9dde8;
    --coin-a: #1c1f2b;
    --coin-b: #3f7ff0;
    --coin-c: #2a3fbf;
    --art-gold: #c99a3a;
    --art-green: #2f6a3a;
    --art-brown: #7a4a2a;
  }
  * { box-sizing: border-box; margin: 0; padding: 0; }
  html, body { width: 1200px; height: 514px; overflow: hidden; background: var(--bg-deep); }
  .banner {
    position: relative;
    width: 1200px;
    height: 514px;
    overflow: hidden;
    font-family: "Poppins", sans-serif;
    color: var(--text-white);
    background:
      radial-gradient(ellipse 380px 300px at 820px 230px, var(--bg-glow) 0%, rgba(23,48,106,0) 100%),
      radial-gradient(ellipse 200px 110px at 110px 30px, rgba(255,255,255,0.10) 0%, rgba(255,255,255,0) 100%),
      radial-gradient(ellipse 200px 110px at 1090px 30px, rgba(255,255,255,0.08) 0%, rgba(255,255,255,0) 100%),
      linear-gradient(180deg, var(--bg-navy) 0%, var(--bg-deep) 100%);
  }
  .brand {
    position: absolute;
    left: 111px;
    top: 50px;
    display: flex;
    align-items: center;
    gap: 12px;
    height: 54px;
    padding: 0 22px 0 0;
  }
  .brand-dot {
    width: 38px; height: 38px; border-radius: 50%;
    background: linear-gradient(135deg, #3a7bff, #27d3c3);
  }
  .brand-name { font-size: 30px; font-weight: 700; letter-spacing: 0.5px; }
  .headline {
    position: absolute;
    left: 109px;
    top: 140px;
    font-size: 53px;
    font-weight: 700;
    line-height: 60px;
    letter-spacing: 0.3px;
    text-transform: uppercase;
  }
  .coins {
    position: absolute;
    left: 111px;
    top: 290px;
    display: flex;
    gap: 14px;
  }
  .coin {
    width: 51px; height: 51px; border-radius: 50%;
    border: 2px solid var(--coin-ring);
  }
  .coin--orb { background: var(--coin-a); }
  .coin--zmtk { background: radial-gradient(circle, var(--coin-b) 0%, #6a4ee8 100%); }
  .coin--qv { background: radial-gradient(circle, #ffffff 0%, #dfe6ff 60%, var(--coin-c) 100%); }
  .selling-points {
    position: absolute;
    left: 112px;
    top: 360px;
    font-size: 17px;
    font-weight: 400;
    display: flex;
    gap: 7px;
    align-items: center;
  }
  .selling-points .sep { color: var(--accent-teal); font-size: 14px; }
  .cta {
    position: absolute;
    left: 116px;
    top: 407px;
    width: 128px;
    height: 43px;
    transform: skewX(-12deg);
    border-radius: 5px;
    background: linear-gradient(90deg, var(--btn-start), var(--btn-end));
    display: flex; align-items: center; justify-content: center;
  }
  .cta span { transform: skewX(12deg); font-size: 17px; font-weight: 600; }
  .hero-art {
    position: absolute;
    left: 520px;
    top: 34px;
    width: 600px;
    height: 472px;
    border-radius: 40px;
    background:
      radial-gradient(ellipse 120px 200px at 300px 160px, var(--art-green) 0%, rgba(47,106,58,0) 100%),
      radial-gradient(ellipse 260px 110px at 300px 300px, var(--art-gold) 0%, rgba(201,154,58,0) 100%),
      radial-gradient(ellipse 280px 120px at 300px 410px, var(--art-brown) 0%, rgba(122,74,42,0) 100%);
    opacity: 0.9;
  }
</style>
</head>
<body>
  <main class="banner">
    <div class="brand">
      <div class="brand-dot"></div>
      <span class="brand-name">QV Wager</span>
    </div>

    <h1 class="headline">Bet on all<br>sports battle</h1>

    <div class="coins" aria-label="Supported coins: ORB, ZMTK, QV">
      <div class="coin coin--orb"></div>
      <div class="coin coin--zmtk"></div>
      <div class="coin coin--qv"></div>
    </div>

    <p class="selling-points">
      <span>Best Odds</span><span class="sep">•</span>
      <span>Be the Bookmaker</span><span class="sep">•</span>
      <span>Own the House</span>
    </p>

    <a class="cta" href="#"><span>sign in</span></a>

    <div class="hero-art" role="img" aria-label="Illustration of a smartphone showing a stadium with gold coins, surrounded by sports balls, a shuttlecock, a puck and coin stacks, with gold 'Sports Betting' lettering"></div>
  </main>
</body>
</html>
```